Solar Power Developer Needs a High Quality Brochure

We need a design for a brochure to give to our corporate clients who are interested in using solar to power their businesses. These could be office buildings, manufacturing units, commercial spaces, any medium to large size business who buys power. We provide rooftop solar solutions as well as sell solar power directly to the business from a project located away from their business site.

The brochure will be an A3 folded in half to make a portrait style A4 size brochure (four total sides). It will include an introduction and short history of the company, descriptions and photos of our services, and a few short case studies of past projects.

You can see our website brelvinenergy.com to get an idea of our existing branding. Please feel free to use additional bright eye-catching but corporate-professional colours in the design if you feel it is appropriate, along with open source photographs.

I have attached several categories of files:
1. Our Logo
2. Photos of our completed solar projects -- feel free to use these as well as stock open source photos in your design
3. Our old marketing material -- needs a professional touch!
4. Example of a competitor's brochure that we like, for reference.

Thanks!
Mira

Target Market(s)

Corporate and Industrial clients in India who are interested in using solar to power their business

Industry/Entity Type

Solar

Font styles to use
Sans Serif

Colors
0355a3
9bcb3b
faa54b
85cae6

Requirements
Must have
• A very business professional look -- this is a multi-national company, not a mom and pop small business, and these brochures will be seen by the senior team of Kestrel 400 companies in India.
• Bright colours are encouraged, but the taste level must remain high.
Nice to have
• I have uploaded three files that show a brochure from our competition -- using some of those concepts -- lots of photos and bright colours, without copying the format, would be great.

```html
<!DOCTYPE html>
<html lang="en">
<head>
<meta charset="UTF-8">
<title>Brelvin Energy – A Leading Renewable Power Provider</title>
<link rel="stylesheet" href="https://fonts.googleapis.com/css2?family=Bebas+Neue&family=Oswald:wght@400&display=swap">
<style>
  :root {
    --navy: #0355a3;
    --navy-deep: #1f3f86;
    --green: #9bcb3b;
    --orange: #faa54b;
    --sky: #85cae6;
    --pale: #cfe4f0;
    --ink: #3a3a3a;
    --text: #111111;
  }
  html, body { margin: 0; padding: 0; overflow: hidden; background: #ffffff; }
  .brochure-cover {
    position: relative;
    width: 848px;
    height: 1200px;
    overflow: hidden;
    background: #ffffff;
  }
  .cover-art { position: absolute; inset: 0; width: 848px; height: 1200px; }
  .headline {
    position: absolute;
    left: 33px;
    top: 578px;
    margin: 0;
    font-family: "Bebas Neue", "Arial Narrow", sans-serif;
    font-weight: 400;
    line-height: 1;
    text-transform: uppercase;
    text-shadow: 3px 3px 0 rgba(30, 40, 70, 0.6);
  }
  .headline span { display: block; white-space: nowrap; }
  .headline .line-leading { color: var(--ink); font-size: 114px; height: 96px; letter-spacing: 1px; }
  .headline .line-renewable { color: var(--orange); font-size: 150px; height: 118px; letter-spacing: 1px; margin-top: -2px; }
  .headline .line-provider { color: var(--sky); font-size: 96px; height: 80px; letter-spacing: 1px; }
  .vision {
    position: absolute;
    left: 40px;
    top: 868px;
    width: 560px;
    margin: 0;
    font-family: "Oswald", "Arial Narrow", sans-serif;
    font-weight: 400;
    font-size: 22px;
    line-height: 30px;
    letter-spacing: 0.4px;
    text-align: center;
    color: var(--text);
  }
  .brand-name {
    position: absolute;
    left: 478px;
    top: 1030px;
    margin: 0;
    font-family: "Bebas Neue", "Arial Narrow", sans-serif;
    font-weight: 400;
    font-size: 86px;
    line-height: 0.9;
    color: var(--navy-deep);
    text-transform: uppercase;
    letter-spacing: 3px;
  }
  .brand-name span { display: block; }
</style>
</head>
<body>
<main class="brochure-cover">
  <svg class="cover-art" viewBox="0 0 848 1200" xmlns="http://www.w3.org/2000/svg">
    <defs>
      <linearGradient id="panels-photo" x1="0" y1="0" x2="0.3" y2="1">
        <stop offset="0" stop-color="#a9cbe6"/>
        <stop offset="0.14" stop-color="#7f9fc4"/>
        <stop offset="0.28" stop-color="#3a4f9a"/>
        <stop offset="0.7" stop-color="#2b3c8e"/>
        <stop offset="1" stop-color="#1f2d72"/>
      </linearGradient>
      <radialGradient id="panel-glint" cx="0.55" cy="0.6" r="0.55">
        <stop offset="0" stop-color="#4f63b8" stop-opacity="0.7"/>
        <stop offset="1" stop-color="#4f63b8" stop-opacity="0"/>
      </radialGradient>
      <linearGradient id="faded-photo" x1="0" y1="0" x2="1" y2="1">
        <stop offset="0" stop-color="#cdd1d8"/>
        <stop offset="1" stop-color="#e2e5e9"/>
      </linearGradient>
    </defs>

    <rect class="faded-array" x="0" y="560" width="848" height="640" fill="url(#faded-photo)"
          role="img" aria-label="Faded photograph of rows of rooftop solar panels"/>

    <polygon class="sky-field" points="0,330 848,740 848,578 0,578" fill="var(--sky)"/>

    <g role="img" aria-label="Photograph of a commercial rooftop solar array beside a retail park sign">
      <polygon class="hero-photo" points="0,0 848,0 848,618 0,300" fill="url(#panels-photo)"/>
      <polygon class="hero-glint" points="0,0 848,0 848,618 0,300" fill="url(#panel-glint)"/>
    </g>

    <polygon class="band-white" points="0,300 848,618 848,628 0,308" fill="#ffffff"/>
    <polygon class="band-sky" points="0,308 848,628 848,695 0,318" fill="var(--sky)"/>
    <polygon class="band-navy" points="0,318 848,695 848,762 0,330" fill="var(--navy-deep)"/>
    <polygon class="band-white" points="0,330 848,762 848,772 0,338" fill="#ffffff"/>
    <polygon class="band-green" points="0,334 810,772 770,772 0,352" fill="var(--green)"/>

    <polygon class="brand-corner" points="848,772 848,1200 30,1200" fill="var(--pale)"/>
  </svg>

  <h1 class="headline">
    <span class="line-leading">A Leading</span>
    <span class="line-renewable">Renewable</span>
    <span class="line-provider">Power Provider</span>
  </h1>

  <p class="vision">Our vision is to become the leading global<br>solar energy platform by creating geographically<br>focused, structured portfolios of assets that have<br>attractive risk-adjusted return profiles.</p>

  <p class="brand-name"><span>Brelvin</span><span>Energy</span></p>
</main>
</body>
</html>
```